Etiketten-Design für Weine
Zielgruppe
Wir sind ein kleines Familien-Weingut Nahe Bernkastel-Kues an der Mosel. Wir erzeugen auf 5,5ha ca. 40-50 TSD Flaschen Wein. Dabei legen wir Wert auf eine naturnahe Bewirtschaftung und eine gute Qualität der Weine. Die wichtigste Rebsorte ist der Riesling. Ansonsten steht die Mosel vor allem für Schieferstein, Steillagen, schöne Landschaft. Die Vermarktung erfolgt fast ausschließlich an Privatkunden. Die Kunden sind i. d. R. mind. 40 Jahre bis 70 Jahre alt gehören mind. der Mittelschicht an; Akademiker und Personen mit Dr.-Titel sind stärker repräsentiert als im Bundesdurchschnitt. Die Vermarktung ist stark Personengebunden: Ich als Winzer bin meist persönlich im Gespräch mit den Kunden.
Aufgabenstellung
Bei dem Entwurf geht es mehr um eine 'kleinen Relaunch'. Bevor Anfang Januar 2021 neue Etiketten gedruckt werden für den neuen Jahrgang, soll das Design nochmals überdacht werden. Hin und wieder werde ich angesprochen von Seiten der Kundschaft; das bisherige Etikett wird anscheinend eher als altbacken wahrgenommen.
Grundsätzlich besteht das Etikett aus dem Logo (farbiger Balken, Hauszeichnung, Schriftzug Morgart-Wessel) und dem weißen Feld mit der Weinbezeichnung darunter. Für den goldenen Rahmen und den Schriftzug Morgart-Wessel wird Heißfolienprägung verwendet. Grün=Basisweine/Literflasche; rot=Hauptlinie ; lila=Premiumlinie ; schwarz=nur für den Rotwein ; Fritz am Fluss (Perlwein) ist ein Sonderetikett mit einem Acrylbild und der Quellgrün Traubensaft erhält jedes Jahr eine neues Foto der Traubenleser. Die stets verwendete Schriftart ist Windows Garamond.
Grundsätzlich würde ich an dem Logo (farbiger Balken mit Hauszeichnung und Schriftzug Weingut Morgart-Wessel) eigentlich gerne festhalten. Da dieses Logo bereits überall Verwendung findet (Broschüre, Visitenkarten, Briefbogen, Weingläser, Weinstand, Website, etc.). Lediglich der goldene Rahmen steht zur Disposition (der findet - außer beim Etikett - sonst keine Verwendung). Gestaltungsmöglichkeit sehe ich in dem weißen Feld unter dem Logo. Da bin ich für alles offen. Mögliche Ansatzpunkte wären Herkunft oder Personen oder einfach grafische Elemente/Effekte um das Etikett aufzuwerten. Da ich bereits mit den verschiedenen Farben (grün/rot/lila/schwarz) arbeite, würde ich an dieser Stelle nicht zusätzlich weitere Farben ins Spiel bringen. Wichtig sind mir die prägnanten Weinnamen (Dorfgeflüster, Sonne Drei, Ruhepol, Feinste Kufe, usw.) Die gesetzlich notwendigen Angaben befinden sich jedoch auf dem Rückenetikett. Das gesamte Weinsortiment kann auch angeschaut werden im Shop unter www.morgart-wessel.de

```html
<!DOCTYPE html>
<html lang="de">
<head>
<meta charset="utf-8">
<title>Morgart-Wessel – Riesling Feinste Kufe 2018</title>
<link rel="stylesheet" href="https://fonts.googleapis.com/css2?family=EB+Garamond:wght@400;500&family=Inter:wght@300;400;600&display=swap">
<style>
  :root {
    --page-bg: #f4f4f2;
    --label-white: #f3f3f5;
    --label-shade: #e6e6ea;
    --brand-gold: #9a7240;
    --text-dark: #3a3a3c;
    --text-soft: #6b6b70;
    --sketch-tone: #d4d4d8;
    --premium-purple: #7c6a80;
    --premium-deep: #2a2530;
    --premium-black: #121214;
  }
  * { margin: 0; padding: 0; box-sizing: border-box; }
  html, body {
    width: 900px;
    height: 1200px;
    overflow: hidden;
    background: var(--page-bg);
  }
  .canvas {
    position: relative;
    width: 900px;
    height: 1200px;
  }
  .wine-label {
    position: absolute;
    left: 106px;
    top: 183px;
    width: 688px;
    height: 835px;
    background: linear-gradient(90deg, var(--label-white) 0%, #fafafb 45%, var(--label-shade) 100%);
    box-shadow: 0 2px 14px rgba(0,0,0,0.08);
  }
  .estate-house {
    position: absolute;
    left: 218px;
    top: 166px;
    width: 253px;
    height: 192px;
    background: linear-gradient(180deg, #e2e2e6 0%, var(--sketch-tone) 100%);
    border-radius: 2px;
  }
  .estate-name {
    position: absolute;
    left: 0;
    right: 0;
    top: 392px;
    text-align: center;
    font-family: "EB Garamond", Garamond, serif;
    font-weight: 500;
    font-size: 35px;
    letter-spacing: 0.01em;
    color: var(--brand-gold);
  }
  .wine-details {
    position: absolute;
    left: 0;
    right: 0;
    top: 634px;
    text-align: center;
    font-family: "Inter", Arial, sans-serif;
    font-size: 24px;
    line-height: 33px;
    letter-spacing: 0.2em;
  }
  .wine-details .vintage,
  .wine-details .style {
    font-weight: 300;
    color: var(--text-soft);
  }
  .wine-details .grape,
  .wine-details .cuvee {
    font-weight: 600;
    color: var(--text-dark);
  }
  .line-band {
    position: absolute;
    left: 0;
    right: 0;
    top: 776px;
    height: 59px;
    background: linear-gradient(90deg, var(--premium-deep) 0%, var(--premium-purple) 30%, var(--premium-deep) 70%, var(--premium-black) 100%);
  }
</style>
</head>
<body>
  <main class="canvas">
    <section class="wine-label">
      <div class="estate-house" role="img" aria-label="Strichzeichnung des Gutshauses des Weinguts"></div>
      <h1 class="estate-name">Morgart-Wessel</h1>
      <div class="wine-details">
        <p class="vintage">2018</p>
        <p class="grape">Riesling</p>
        <p class="cuvee">Feinste Kufe</p>
        <p class="style">trocken</p>
      </div>
      <div class="line-band"></div>
    </section>
  </main>
</body>
</html>
```